Indian Takeaway Menu

We need a flyer for an existing Indian Takeaway business in dublin Ireland.

We need some upto date style menu may be a A4 sheet folded in 3 layers.

But not folded in landscape side folded from portrait side and typing from portrait side from top, as we type in a word document and then fold the letter in 3 layers.
please amend your designs as everyone have done the same thing which is very boring.

We have a logo we would like to use in front of the menu. Designer have to come up with the colour which will help the logo to stand out. we also have a review in the paper which we would like to use at the back page somewhere.

New ideas are welcome from the designer
Please look at the example menu attached.

City population

Landscape

Font styles to use
Sans Serif

Colors
acd037

Requirements
Must have
• ingredient sign for
• Nuts
• Celiac
• Low fat
• Diary
Nice to have
• attractive

```html
<!DOCTYPE html>
<html lang="en">
<head>
<meta charset="utf-8">
<title>Saffron Lodge – Takeaway Menu</title>
<link href="https://fonts.googleapis.com/css2?family=Arimo:wght@400;700&family=Oswald:wght@500;700&display=swap" rel="stylesheet">
<style>
:root{
  --lime:#b2f53c;
  --ink:#111;
  --chili:#d4201a;
  --leaf:#3f7d63;
  --logo-gold:#f2d21a;
  --photo-a:#c9a15a;
  --photo-b:#7a3a1c;
  --tag-nut:#8a5a2b;
  --tag-gluten:#c98a12;
  --tag-lowfat:#2f8a3a;
  --tag-dairy:#2a5fa8;
}
*{margin:0;padding:0;box-sizing:border-box}
html,body{width:848px;height:1200px;overflow:hidden;background:var(--lime)}
body{position:relative;font-family:"Arimo",Arial,sans-serif;color:var(--ink)}
.panel{position:absolute;border:2px solid var(--ink);border-radius:14px;padding:20px 16px 18px;overflow:hidden;display:flex;flex-direction:column}
.panel::before{content:"";position:absolute;inset:4px;border:1px solid var(--ink);border-radius:10px;pointer-events:none;z-index:2}
.p1{left:12px;top:14px;width:266px;height:572px}
.p2{left:292px;top:14px;width:264px;height:572px}
.p3{left:572px;top:14px;width:266px;height:572px;padding-bottom:6px}
.p4{left:12px;top:614px;width:266px;height:574px}
.p5{left:292px;top:614px;width:264px;height:574px}
.p6{left:572px;top:614px;width:266px;height:574px}
.section-title{font-weight:700;font-size:9.5px;text-align:center;margin:6px 0 8px}
.dish{margin-bottom:8px}
.dish-name{display:flex;align-items:center;font-weight:700;font-size:7.6px}
.dish-name .lead{flex:1;border-bottom:1px dotted var(--ink);margin:0 4px 2px;min-width:8px}
.dish-price{font-weight:700}
.chili{width:14px;height:8px;margin-right:4px}
.dish-desc{font-size:5.6px;line-height:1.3;margin-top:1px}
.tag{display:inline-flex;align-items:center;justify-content:center;width:9px;height:9px;border-radius:50%;color:#fff;font-size:5.5px;font-weight:700;margin-left:3px;flex:none}
.tag-nut{background:var(--tag-nut)}
.tag-gluten{background:var(--tag-gluten)}
.tag-lowfat{background:var(--tag-lowfat)}
.tag-dairy{background:var(--tag-dairy)}
.sub-head{font-weight:700;font-size:7.6px;text-decoration:underline;margin:2px 0 0}
.meal{font-size:7.6px;margin-bottom:12px}
.meal-head{display:flex;font-weight:700}
.meal-head .lead{flex:1;border-bottom:1px dotted var(--ink);margin:0 4px 2px}
.meal ul{list-style:none;padding-left:36px;line-height:1.35}
.photo{border-radius:8px}
.meal-photo{width:228px;height:108px;margin:4px auto 0;background:radial-gradient(circle at 50% 55%,#f4f4f4 0 22%,#8c8c8c 23% 30%,var(--photo-a) 31% 55%,var(--photo-b) 80%)}
.side-list{font-size:7.6px;border-top:1px solid #555}
.side-row{display:flex;justify-content:space-between;padding:2px 4px;border-bottom:1px solid #555;line-height:1.2}
.side-row.indent span:first-child{padding-left:12px}
.kids-row{display:flex;font-weight:700;font-size:7.6px;margin:0 8px 8px}
.kids-row .lead{flex:1;border-bottom:1px dotted var(--ink);margin:0 3px 2px}
.side-photo{flex:1;min-height:0;margin:2px -6px 0;background:linear-gradient(90deg,#e9c27a,#c77a32 30%,#d7b06a 55%,#c4301e 85%,#e25a2c)}
.logo-box{width:176px;height:70px;margin:22px auto 16px;background:var(--logo-gold);border:2px solid var(--ink);display:flex;align-items:center;justify-content:center;gap:8px;flex:none}
.logo-box .mark{width:10px;height:10px;background:var(--ink)}
.logo-box .name{font-family:"Arimo",Arial,sans-serif;font-weight:700;font-size:22px}
.tagline{color:var(--leaf);font-size:12.5px;text-align:center;margin-bottom:8px}
.cooked{color:var(--leaf);font-size:11.5px;text-align:center;margin-bottom:6px}
.phones{display:flex;align-items:center;gap:10px;padding-left:12px}
.phone-icon{width:28px;height:28px}
.phone-list{border-left:1px solid var(--ink);padding-left:12px;font-weight:700;font-size:23px;line-height:1.3}
.hours{font-family:"Oswald",sans-serif;font-weight:700;font-size:12.5px;text-align:center;line-height:1.35;margin-top:10px}
.delivery{color:var(--leaf);font-size:9.5px;text-align:center;margin:12px 0 14px}
.addr{display:flex;align-items:center;gap:12px;padding-left:20px}
.addr svg{width:20px;height:28px}
.addr p{border-left:1px solid var(--ink);padding-left:12px;color:var(--leaf);font-size:12px;line-height:1.4}
.web{display:flex;align-items:center;gap:12px;padding-left:20px;margin-top:18px}
.web svg{width:20px;height:20px}
.web p{border-left:1px solid var(--ink);padding-left:12px;color:var(--leaf);font-size:12.5px;line-height:26px}
.allergen-key{display:flex;justify-content:center;flex-wrap:wrap;gap:4px 10px;margin-top:14px;font-size:7.5px}
.allergen-key span{display:inline-flex;align-items:center;gap:3px}
.allergen-key .tag{margin-left:0}
</style>
</head>
<body>

<svg width="0" height="0" style="position:absolute">
  <defs>
    <symbol id="chili" viewBox="0 0 14 8"><path d="M1 5 C4 8 10 7 12 3 L13 1 L11 2 C9 5 5 5 1 5Z" fill="#d4201a"/><path d="M12 3 L14 0" stroke="#2a7a1a" stroke-width="1.2"/></symbol>
  </defs>
</svg>

<!-- Prawn & vegetarian dishes -->
<section class="panel p1">
  <div class="dish"><div class="dish-name">29.Tandoori Prawn Masala (Mild)<span class="tag tag-dairy">D</span><span class="lead"></span><span class="dish-price">€10.00</span></div><p class="dish-desc">Sauteed prawns in a smooth creamy sauce flavoured with kasoori methi &amp; tandoori spices</p></div>
  <div class="dish"><div class="dish-name">30.Prawn Karahi<span class="lead"></span><svg class="chili"><use href="#chili"/></svg><span class="dish-price">€10.00</span></div><p class="dish-desc">Succulent prawns cooked with green peppers, spring onion, tomatoes &amp; whole spices</p></div>
  <div class="dish"><div class="dish-name">31.Goan Prawn Curry<span class="lead"></span><svg class="chili"><use href="#chili"/></svg><span class="dish-price">€10.50</span></div><p class="dish-desc">Fisherman's favourite prawn curry flavoured with curry leaves, coconut, crushed spices &amp; fresh herbs</p></div>
  <div class="dish"><div class="dish-name">32.Prawn Biryani<span class="lead"></span><svg class="chili"><use href="#chili"/></svg><span class="dish-price">€10.00</span></div><p class="dish-desc">Shrimp prawn cooked with egg, green peas &amp; onion</p></div>
  <div class="dish"><div class="dish-name">33. Chicken Dupiaza<span class="lead"></span><span class="dish-price">€8.00</span></div><p class="dish-desc">Chicken breast pieces cooked with fresh tomato &amp; sliced onions</p></div>
  <div class="dish"><div class="dish-name">34. Chicken Rogan Josh<span class="lead"></span><span class="dish-price">€8.00</span></div><p class="dish-desc">A red chicken curry prepared with fresh herb &amp; spices, a delicacy from Kashmir</p></div>
  <div class="dish"><div class="dish-name">35. Chicken Madras<span class="lead"></span><span class="dish-price">€8.00</span></div><p class="dish-desc">Chicken cooked in a hot spicy sauce</p></div>
  <div class="dish"><div class="dish-name">36. Tarkari Makhani<span class="tag tag-dairy">D</span><span class="lead"></span><span class="dish-price">€8.00</span></div><p class="dish-desc">Mixed seasonal vegetables in a smooth butter, cream &amp; tomato sauce</p></div>
  <h2 class="section-title">Vegetarian Dishes</h2>
  <div class="dish"><div class="dish-name">37.Gajar Mater Paneer<span class="tag tag-dairy">D</span><span class="lead"></span><svg class="chili"><use href="#chili"/></svg><span class="dish-price">€8.00</span></div><p class="dish-desc">Mild. A colourful combination of chopped carrots, peas &amp; Indian cheese in semi-dry sauce - chef's special for vegetarians (recommended)</p></div>
  <div class="dish"><div class="dish-name">38.Dhingri Dulma<span class="tag tag-dairy">D</span><span class="lead"></span><svg class="chili"><use href="#chili"/></svg><span class="dish-price">€10.50</span></div><p class="dish-desc">Mild. Fresh mushroom &amp; Indian cheese fried with onion, ginger &amp; garlic in mild spices</p></div>
  <div class="dish"><div class="dish-name">39.Dum Wale Aloo<span class="lead"></span><span class="dish-price">€7.70</span></div><p class="dish-desc">Potatoes cooked with fresh ginger, garlic, onions, tomatoes curry leaves &amp; slow cooked with cumin flavoured yoghurt</p></div>
  <div class="dish"><div class="dish-name">40.Karahi Paneer<span class="tag tag-dairy">D</span><span class="lead"></span><span class="dish-price">€7.70</span></div><p class="dish-desc">A Semi-dry and colourful curry is prepared using homemade Indian cheese (paneer)</p></div>
  <div class="dish"><div class="dish-name">41.Paneer Jalferzi<span class="tag tag-dairy">D</span><span class="lead"></span><span class="dish-price">€8.00</span></div><p class="dish-desc">Stir fried homemade cottage cheese &amp; peppers with roasted coriander seeds, fresh tomato, onion &amp; green chillies</p></div>
  <div class="dish"><div class="dish-name">42.Sambhar Vegetable Curry<span class="tag tag-lowfat">L</span><span class="lead"></span><span class="dish-price">€7.70</span></div><p class="dish-desc">Mixed seasonal vegetable curry cooked with little lentil, coconut, curry leaves, mustard &amp; fresh coriander (recommended)</p></div>
  <div class="dish"><div class="dish-name">43.Aloo Saag Haryali<span class="tag tag-lowfat">L</span><span class="lead"></span><span class="dish-price">€7.70</span></div><p class="dish-desc">Pan fried potatoes &amp; spinach, flavoured with kasoori methi &amp; fresh coriander</p></div>
  <div class="dish"><div class="dish-name">44.Vegetable Biryani Orraita<span class="lead"></span><span class="dish-price">€8.50</span></div><p class="dish-desc">Basmati Rice cooked with mixed seasonal vegetables, fresh herbs, spices &amp; fried golden onion. Served with your choice of mixed vegetable</p></div>
</section>

<!-- Meal deals -->
<section class="panel p2">
  <h2 class="section-title" style="margin-top:14px;margin-bottom:12px">Meal Deal</h2>
  <div class="meal"><div class="meal-head">Set Meal A For 1 (Vegetarian)<span class="lead"></span>€14.00</div>
    <ul><li>Gole bhajia</li><li>Sambhar vegetable curry</li><li>Pilau rice</li><li>Naan</li><li>Poppadoms &amp; spiced onion</li><li>Soft Drink</li></ul></div>
  <div class="meal"><div class="meal-head">Set Meal B For 1 (Non Vegetarian)<span class="lead"></span>€16.00</div>
    <ul><li>Chicken tikka</li><li>Chicken tikka masala</li><li>Pilau rice</li><li>Naan</li><li>Poppadom &amp; spiced onion</li><li>Soft Drink</li></ul></div>
  <div class="meal"><div class="meal-head">Set Meal For 2<span class="lead"></span>€25.00</div>
    <ul><li>Gole bhajia</li><li>Chicken tikka</li><li>Chicken tikka masala</li><li>Lamb Roganjosh</li><li>Pilau rice</li><li>naan</li><li>Poppadom &amp; spiced onion</li><li>2 Soft Drinks</li></ul></div>
  <div class="meal"><div class="meal-head">Set Meal for 3/4<span class="lead"></span>€39.00</div>
    <ul><li>Gole bhajia</li><li>Vegetable samosa</li><li>Chicken tikka</li><li>Chicken Tikka Masala</li><li>Prawn Karahi</li><li>Sambhar Vegetable</li><li>2 Pilau Rice</li><li>Poppadom &amp; spiced onion</li><li>2 Soft Drinks</li></ul></div>
  <div class="photo meal-photo" role="img" aria-label="Photo of a thali platter with rice, curries and dips"></div>
</section>

<!-- Naan, sides, kids -->
<section class="panel p3">
  <h2 class="section-title" style="margin-top:10px;margin-bottom:10px">Nan Bread &amp; Side Orders</h2>
  <div class="side-list">
    <div class="side-row"><span>1.Naan</span><span>€1.90</span></div>
    <div class="side-row"><span>2.Garlic Naan</span><span>€2.50</span></div>
    <div class="side-row indent"><span>* Garlic Chilli Naan</span><span>€3.00</span></div>
    <div class="side-row"><span>3. Peshwari Naan</span><span>€2.70</span></div>
    <div class="side-row"><span>4. Keema Naan</span><span>€3.00</span></div>
    <div class="side-row"><span>5.Coriander Naan</span><span>€2.50</span></div>
    <div class="side-row"><span>6.Blue Cheese Naan</span><span>€2.50</span></div>
    <div class="side-row indent"><span>* G.O.C.</span><span>€3.00</span></div>
    <div class="side-row"><span>7. Boiled Basmati</span><span>€2.00</span></div>
    <div class="side-row"><span>8. Pilau Rice</span><span>€2.10</span></div>
    <div class="side-row"><span>9.Vegetable &amp; Fruit Pilau</span><span>€2.50</span></div>
    <div class="side-row"><span>10. Poppodum(2) &amp; Spiced Onion</span><span>€2.00</span></div>
    <div class="side-row"><span>11.Onion,Mint &amp; Cucumber Riata</span><span>€2.00</span></div>
    <div class="side-row"><span>12. Mix Pickle Dips</span><span>€2.00</span></div>
    <div class="side-row indent"><span>* Bombay Aloo</span><span>€5.00</span></div>
    <div class="side-row indent"><span>* Tarka Dal Lentil curry</span><span>€4.50</span></div>
    <div class="side-row indent"><span>* Saag Paneer Spinach &amp; Indian chees</span><span>€5.50</span></div>
    <div class="side-row indent"><span>* Aloo Ghobi side</span><span>€5.00</span></div>
    <div class="side-row indent"><span>* Aloo Choley Masala Side</span><span>€5.00</span></div>
  </div>
  <h2 class="section-title" style="margin-top:12px;margin-bottom:8px">Kids Meals</h2>
  <div class="kids-row">Kids Chicken Korma with rice<span class="lead"></span>€6.00</div>
  <div class="kids-row">Kids Chic Tikka Masala with rice<span class="lead"></span>€6.00</div>
  <div class="kids-row">Kids Cheese Tikka Naan<span class="lead"></span>€3.00</div>
  <div class="kids-row">Doner Kebab in Nan Bread<span class="lead"></span>€7.00</div>
  <div class="photo side-photo" role="img" aria-label="Photo strip of paneer, biryani, curry and tandoori dishes"></div>
</section>

<!-- Chicken & lamb dishes -->
<section class="panel p4">
  <div class="dish"><div class="dish-name">****Chicken Dansak<span class="lead"></span><span class="dish-price">€8.50</span></div><p class="dish-desc">Sweet and sour sauce prepared with mixed fruit and spices</p></div>
  <div class="dish"><div class="dish-name">14.Chicken Saag<span class="lead"></span><span class="dish-price">€9.50</span></div><p class="dish-desc">Chicken breast pieces cooked with spinach, fresh Herbs, tomato tangy sauce and coriander</p></div>
  <div class="dish"><div class="dish-name">15.Chicken Royale Korma<span class="tag tag-nut">N</span><span class="tag tag-dairy">D</span><span class="lead"></span><span class="dish-price">€8.50</span></div><p class="dish-desc">Chopped breast of chicken cooked in a rich creamy sauce with coconut, probably most popular among Irish</p></div>
  <div class="dish"><div class="dish-name">16. Saffron Lodge Chicken Curry<span class="lead"></span><span class="dish-price">€8.50</span></div><p class="dish-desc">Traditional Indian chicken curry to suit most Palates mild, medium or hot, you choose</p></div>
  <div class="dish"><div class="dish-name">17.Chicken Karahi<span class="lead"></span><svg class="chili"><use href="#chili"/></svg><span class="dish-price">€8.00</span></div><p class="dish-desc">Diced chicken prepared with green peppers, spring onion, tomatoes and Indian whole spices</p></div>
  <div class="dish"><div class="dish-name">18.Chicken Tikka Masala<span class="tag tag-dairy">D</span><span class="lead"></span><span class="dish-price">€8.00</span></div><p class="dish-desc">Tender chicken tikka cooked in a smooth creamy tomato sauce, Most popular</p></div>
  <div class="dish"><div class="dish-name">19. South Indian Garlic Chilli<span class="lead"></span><svg class="chili"><use href="#chili"/></svg><span class="dish-price">€8.00</span></div><p class="dish-desc">Tasty red chicken curry loaded with garlic, ground Spices, fresh herbs and green chillies.</p></div>
  <div class="dish"><div class="dish-name">20.Chicken Dahiwala<span class="lead"></span><svg class="chili"><use href="#chili"/></svg><span class="dish-price">€8.00</span></div><p class="dish-desc">Amazingly spicy chicken curry with fresh coconut, yogurt, green chillies, ginger and herbs</p></div>
  <div class="dish"><div class="dish-name">21.ChickenVegetable &amp; Nut Curry<span class="tag tag-nut">N</span><span class="lead"></span><span class="dish-price">€8.50</span></div><p class="dish-desc">Boneless chicken breast pieces sauted with fresh vetetables, nuts and herbs in a smooth creamy sauce</p></div>
  <div class="dish"><div class="dish-name">22.Chicken Biryani<span class="lead"></span><span class="dish-price">€9.00</span></div><p class="dish-desc">Breast of chicken chopped and cooked with Basmati rice, fresh herbs, spices and fried onion accompanied with vetetable curry.</p></div>
  <p class="sub-head">Lamb Dishes</p>
  <div class="dish"><div class="dish-name">23. Lamb Bhuna<span class="lead"></span><span class="dish-price">€9.50</span></div><p class="dish-desc">Spring lamb pieces sauted with spring onion, tomatoes, crushed black pepper and fresh herbs</p></div>
  <div class="dish"><div class="dish-name">24. Haandi Gosht<span class="lead"></span><span class="dish-price">€9.50</span></div><p class="dish-desc">Lamb cooked with chunky pepper, onion, tomatoes, mushrooms, green chilli &amp; fresh coriander</p></div>
  <div class="dish"><div class="dish-name">25. Palak Gosht<span class="lead"></span><span class="dish-price">€9.50</span></div><p class="dish-desc">Pan-fried lamb pieces cooked with spinach, fresh herbs and coriander</p></div>
  <div class="dish"><div class="dish-name">26. Lamb Roganjosh<span class="lead"></span><svg class="chili"><use href="#chili"/></svg><span class="dish-price">€9.50</span></div><p class="dish-desc">A red lamb curry prepared with fresh herb and spices, a delicacy from Kashmir</p></div>
  <div class="dish"><div class="dish-name">27. Lamb Kohlapuri<span class="lead"></span><span class="dish-price">€10.00</span></div><p class="dish-desc">A hot lamb dish from South Coast of India Flavoured with yoghurt and coconut</p></div>
  <div class="dish"><div class="dish-name">**Lamb Jalferzi<span class="lead"></span><span class="dish-price">€10.00</span></div><p class="dish-desc">A semi dry dish of lamb, tossed with strips of onions, assorted bell pepper tomatoes and flavoured with crushed coriander seeds and dry fenugreek</p></div>
  <div class="dish"><div class="dish-name">28.Gosht Biryani Sofyani<span class="lead"></span><span class="dish-price">€10.50</span></div><p class="dish-desc">Basmati rice cooked with cubed lamb Flavoured with fresh mint and fried onion, accompanied with vegetable curry.</p></div>
</section>

<!-- Starters -->
<section class="panel p5">
  <h2 class="section-title">Veg Starters</h2>
  <div class="dish"><div class="dish-name">1.Onion Bhajia<span class="tag tag-gluten">G</span><span class="lead"></span><span class="dish-price">€4.00</span></div><p class="dish-desc">Sliced Onions, fresh spinach and herbs fried with gram flour until golden.</p></div>
  <div class="dish"><div class="dish-name">2.Vegetable Samosa<span class="lead"></span><span class="dish-price">€4.00</span></div><p class="dish-desc">Crispy handmade pastry filled with potato and peas deep fried with herb until golden.</p></div>
  <div class="dish"><div class="dish-name">3. Palak Kachori<span class="lead"></span><span class="dish-price">€4.00</span></div><p class="dish-desc">Golden fried cakes of fresh spinach and yellow chana lentil, served with tamarind dip. Recommended</p></div>
  <div class="dish"><div class="dish-name">4.Veg Pakora<span class="tag tag-gluten">G</span><span class="lead"></span><span class="dish-price">€4.00</span></div><p class="dish-desc">Cauliflower, potato and onion golden fried with Gram flour batter.</p></div>
  <div class="dish"><div class="dish-name">*** Aloo Chana Chat<span class="tag tag-lowfat">L</span><span class="lead"></span><span class="dish-price">€3.50</span></div><p class="dish-desc">Aloo chana chaat is a low fat snack made with boiled chickpeas, potatoes and chaat masala</p></div>
  <h2 class="section-title">Meat Starters</h2>
  <div class="dish"><div class="dish-name">5.Keema Singhara<span class="lead"></span><span class="dish-price">€4.00</span></div><p class="dish-desc">Crispy handmade pastry filled with lamb mince,fresh herbs and spices accompanied with a tongue tingling mint chutney</p></div>
  <div class="dish"><div class="dish-name">6.PrawnChatpate<span class="lead"></span><span class="dish-price">€5.00</span></div><p class="dish-desc">Pan-fried prawns cooked with tangy lemon and coriander sauce</p></div>
  <div class="dish"><div class="dish-name">7.ChickenTikka<span class="tag tag-lowfat">L</span><span class="lead"></span><span class="dish-price">€4.50</span></div><p class="dish-desc">Tender pieces of chicken marinated, cooked in Clay Oven and served with salad and a Mint dip.</p></div>
  <div class="dish"><div class="dish-name">8. Seekh Kebab<span class="lead"></span><span class="dish-price">€5.00</span></div><p class="dish-desc">A lamb mince barbecued delicacy, served with Salad and a mint dip</p></div>
  <div class="dish"><div class="dish-name">9. Chicken Pakora<span class="lead"></span><span class="dish-price">€ 5.00</span></div><p class="dish-desc">Boneless pieces of chicken coated in batter/spice, deep fried.</p></div>
  <div class="dish"><div class="dish-name">10. Chicken Wings<span class="lead"></span><span class="dish-price">€5.00</span></div><p class="dish-desc">Clay Oven Dishes Served with Nan and Curry Sauce</p></div>
  <div class="dish"><div class="dish-name">10.Tandoori Chicken (Half)<span class="lead"></span><span class="dish-price">€9.50</span></div><p class="dish-desc">Spring chicken marinated with yoghurt and tandoori spices, grilled in clay oven</p></div>
  <div class="dish"><div class="dish-name">11Chicken Tikka<span class="lead"></span><span class="dish-price">€9.50</span></div><p class="dish-desc">Tender breast pieces of chicken marinated and cooked in a clay oven</p></div>
  <div class="dish"><div class="dish-name">12. Seekh Kebab<span class="lead"></span><span class="dish-price">€10.00</span></div><p class="dish-desc">A lamb mince barbecued delicacy</p></div>
  <div class="dish"><div class="dish-name">13. Saffron Lodge's Mix Grill<span class="lead"></span><span class="dish-price">€10.50</span></div><p class="dish-desc">2 pcs of chicken tikka, 2 pcs seekh kebab, 2 pcs battered prawns, 1 pc tandoori chicken</p></div>
</section>

<!-- Front cover -->
<section class="panel p6">
  <div class="logo-box"><span class="mark"></span><span class="name">Saffron Lodge</span></div>
  <p class="tagline">Authentic Indian Takeaway</p>
  <p class="cooked">All our meals are cooked to order.</p>
  <div class="phones">
    <svg class="phone-icon" viewBox="0 0 28 28" aria-hidden="true"><circle cx="14" cy="14" r="12" fill="none" stroke="#111" stroke-width="1.5"/><path d="M9 8 l3 -1 l2 4 l-2 1.5 c1 2 2 3 4 4 l1.5 -2 l4 2 l-1 3 c-6 0 -11.5 -5.5 -11.5 -11.5z" fill="#111"/></svg>
    <div class="phone-list"><p>1890 44 21 07</p><p>01 555 0182</p><p>01 555 0196</p></div>
  </div>
  <p class="hours">Open Sun-Wed 5 p.m to 10.00pm<br>Thurs-Sat 5.00pm-10.30pm</p>
  <p class="delivery">Delivery Service available from 5.00p.m</p>
  <div class="addr">
    <svg viewBox="0 0 20 28" aria-hidden="true"><path d="M10 1 a9 9 0 0 1 9 9 c0 7 -9 17 -9 17 s-9 -10 -9 -17 a9 9 0 0 1 9 -9z" fill="#111"/><circle cx="10" cy="10" r="3.5" fill="#b2f53c"/></svg>
    <p>Unit 4, Kestrel Court<br>(Near Harbour Retail)<br>Glenmoor<br>Bayview</p>
  </div>
  <div class="web">
    <svg viewBox="0 0 20 20" aria-hidden="true"><circle cx="10" cy="10" r="8.5" fill="none" stroke="#111" stroke-width="1.3"/><ellipse cx="10" cy="10" rx="4" ry="8.5" fill="none" stroke="#111" stroke-width="1"/><path d="M1.5 10h17M3 5.5h14M3 14.5h14" stroke="#111" stroke-width="1"/></svg>
    <p>www.saffronlodge.ie</p>
  </div>
  <div class="allergen-key">
    <span><i class="tag tag-nut">N</i>Nuts</span>
    <span><i class="tag tag-gluten">G</i>Celiac</span>
    <span><i class="tag tag-lowfat">L</i>Low fat</span>
    <span><i class="tag tag-dairy">D</i>Dairy</span>
  </div>
</section>

</body>
</html>
```